Fence Flyer to Attract More Sales During Winter

We need a new flyer made that we can distribute to residential mailboxes. The flyer is to promote our Frostline Picket Days. We like simply designs, and we would like the flyer to showcase a lot of our fence photos. More of our photos are online at our website at www.getbramblerail.com - our new address needs to also be featured on the flyer - 436 Quillen rd, Monroe, NC 28117. I do want the words "FROSTLINE PICKET DAYS" to be dominate on the flyer with the description "Wood fences starting at $12/FT!" Please look through our Facebook page and our website to gather more photos or information. We are flexible on colors, nothing to fancy - simple flyer design please.

Target Market(s)

Residential homeowners that need a new fence to enclose their yard for safety, security or decorative

Industry/Entity Type

Residential Construction

Font styles to use
Sans Serif

Colors

Designer to choose colors to be used in the design.

Requirements
Must have
• Frostline Picket Days
• Contact information for the business
• "Come visit our outdoor showroom, open 24/7!"
Nice to have
• Photos of our fences - you can find more on our website at www.GetBrambleRail.com or Facebook.com/MeadowlarkRailGPV
Should not have
• Flashy designs

```html
<!DOCTYPE html>
<html lang="en">
<head>
<meta charset="utf-8">
<title>Frostline Picket Days – Bramble Rail Fence</title>
<link rel="stylesheet" href="https://fonts.googleapis.com/css2?family=Big+Shoulders+Stencil+Display:wght@800;900&family=Source+Sans+3:wght@400;600;700&display=swap">
<style>
  :root {
    --navy-deep: #1e1f57;
    --navy-band: #2a2d6c;
    --sky-blue: #3b87c9;
    --accent-orange: #e8882c;
    --white: #ffffff;
    --frame: #c9ccd8;
    --page-bg: #ffffff;
  }
  * { box-sizing: border-box; margin: 0; padding: 0; }
  html, body {
    width: 1017px; height: 1200px;
    overflow: hidden;
    background: var(--page-bg);
  }
  .flyer {
    position: relative;
    width: 1017px; height: 1200px;
    overflow: hidden;
    font-family: "Source Sans 3", Arial, sans-serif;
    color: var(--white);
    background: var(--navy-deep);
  }
  .flyer-shapes {
    position: absolute; inset: 0;
    width: 1017px; height: 1200px;
  }
  .headline {
    position: absolute;
    left: 0; right: 0; top: 552px;
    text-align: center;
    font-family: "Big Shoulders Stencil Display", Impact, sans-serif;
    font-weight: 900;
    font-size: 90px;
    line-height: 1;
    letter-spacing: 1px;
    text-shadow: 0 4px 10px rgba(0, 0, 0, 0.45);
  }
  .offer {
    position: absolute;
    left: 0; right: 0; top: 664px;
    text-align: center;
    font-weight: 600;
    font-size: 34px;
    color: var(--sky-blue);
  }
  .gallery {
    position: absolute;
    left: 0; right: 0; top: 735px;
    height: 200px;
    display: flex;
    justify-content: space-between;
  }
  .gallery-photo {
    width: 329px; height: 200px;
    border: 2px solid var(--frame);
  }
  .gallery-photo.metal {
    background: linear-gradient(180deg, #b7c4cf 0%, #4f6a3a 40%, #7d8a4c 70%, #9a8a5e 100%);
  }
  .gallery-photo.picket {
    background: linear-gradient(180deg, #c9d7e2 0%, #4e7a3c 35%, #6e9146 55%, #c9ab78 75%, #8d6a48 100%);
  }
  .gallery-photo.privacy {
    background: linear-gradient(90deg, #486f34 0%, #6a8f3f 30%, #b58e62 60%, #c9a473 100%);
  }
  .showroom {
    position: absolute;
    left: 0; right: 0; top: 978px;
    text-align: center;
    font-weight: 400;
    font-size: 26px;
    text-transform: uppercase;
    color: var(--accent-orange);
  }
  .footer-contact {
    position: absolute;
    left: 36px; top: 1120px;
    font-size: 19px;
    line-height: 1.35;
  }
  .footer-address {
    position: absolute;
    right: 28px; top: 1120px;
    text-align: right;
    font-size: 19px;
    line-height: 1.35;
  }
  .brand {
    position: absolute;
    left: 312px; top: 1086px;
    display: flex;
    align-items: center;
    gap: 14px;
  }
  .brand-mark {
    width: 52px; height: 52px;
    background: var(--accent-orange);
    flex: none;
  }
  .brand-name {
    font-weight: 700;
    font-size: 27px;
    line-height: 1.1;
    white-space: nowrap;
  }
  .brand-phone {
    font-weight: 700;
    font-size: 32px;
    line-height: 1.1;
  }
  .brand-tagline {
    font-weight: 600;
    font-size: 13px;
    color: var(--accent-orange);
    white-space: nowrap;
  }
</style>
</head>
<body>
<main class="flyer">
  <svg class="flyer-shapes" viewBox="0 0 1017 1200">
    <defs>
      <linearGradient id="heroTones" x1="0" y1="0" x2="0" y2="1">
        <stop offset="0" stop-color="#e9eef5"/>
        <stop offset="0.08" stop-color="#8fb1db"/>
        <stop offset="0.22" stop-color="#a9b7c6"/>
        <stop offset="0.3" stop-color="#8e7a66"/>
        <stop offset="0.36" stop-color="#d9c28a"/>
        <stop offset="0.52" stop-color="#e6d39c"/>
        <stop offset="0.62" stop-color="#d8c189"/>
        <stop offset="0.68" stop-color="#e8edf4"/>
        <stop offset="1" stop-color="#f4f6fa"/>
      </linearGradient>
    </defs>
    <polygon class="hero-photo" role="img"
      aria-label="Photo: new wooden privacy fence beside a brick house in winter snow, icicles hanging along the top"
      points="0,0 1017,0 1017,503 532,397 0,503" fill="url(#heroTones)"/>
    <polygon class="chevron-band" points="0,503 532,397 1017,503 1017,545 532,440 0,545" fill="var(--navy-band)"/>
    <polygon class="footer-band" points="0,1083 532,1038 1017,1083 1017,1200 0,1200" fill="var(--sky-blue)"/>
    <polygon class="footer-edge" points="0,1058 532,1012 1017,1058 1017,1083 532,1038 0,1083" fill="var(--navy-band)"/>
  </svg>

  <h1 class="headline">FROSTLINE PICKET DAYS</h1>
  <p class="offer">Wood fences starting at $12/FT!</p>

  <section class="gallery">
    <div class="gallery-photo metal" role="img" aria-label="Photo: black metal picket fence along a grassy yard with shrubs"></div>
    <div class="gallery-photo picket" role="img" aria-label="Photo: wooden spaced-picket fence enclosing a green lawn"></div>
    <div class="gallery-photo privacy" role="img" aria-label="Photo: tall wooden privacy fence with rose bushes along a garden bed"></div>
  </section>

  <p class="showroom">Come visit our outdoor showroom, open 24/7!</p>

  <div class="footer-contact">
    <p>Contact us Now!</p>
    <p>704-555-0142</p>
  </div>

  <div class="brand">
    <span class="brand-mark"></span>
    <div>
      <p class="brand-name">Bramble Rail Fence</p>
      <p class="brand-phone">704-555-0142</p>
      <p class="brand-tagline">"Because Good Fences Make Good Neighbors"</p>
    </div>
  </div>

  <div class="footer-address">
    <p>www.getbramblerail.com</p>
    <p>436 Quillen rd, Monroe, NC 28117</p>
  </div>
</main>
</body>
</html>
```